Harbourline Strategy Group firm

I need a business card that is succint for a Brisbane based business called Harbourline Strategy Group Pty Ltd.
We bridge the gaps between People, Process and Technology.

We are a specialist operational excellence firm, delivering strategic consulting and business advisory services in six core capabilities, across all industries and all business lines to improve performance, efficiency, profitability, automation and scalability, for clients across Australia &New Zealand.
Updates

Hi Designers, I have uploaded the logo in 3D .png format, to assist in card design.

Target Market(s)

Project Management professionals, IT professionals, corporate and government clients managing transitioning or transformation projects.

Contact Information for Business Card

Harbourline Strategy Group Pty Ltd

Daniel Ferreira
Principal Consultant

mobile: +61 417 260 315
email: daniel@harbourlinestrategygroup.com.au
webpage: www.harbourlinestrategygroup.com

professional services: strategic advisors,

Font styles to use
Sans Serif

Requirements
Must have
• Business name: Harbourline Strategy Group
logo: attached
Contact person: Daniel Ferreira
Title: Principal Consultant
contact details:
mobile +61 417 260
email: daniel@HarbourlineStrategyGroup.com.au
website: HarbourlineStrategyGroup.com

on back side with logo include: A.B.N. 58210947362

professional services offered: Business Analysis, Strategic Advisory
Nice to have
• QR code
Should not have
• contacts picture

```html
<!DOCTYPE html>
<html lang="en">
<head>
<meta charset="utf-8">
<title>Harbourline Strategy Group – Business Card</title>
<link rel="stylesheet" href="https://fonts.googleapis.com/css2?family=Oswald:wght@300;400;500&display=swap">
<style>
  :root {
    --navy: #1f2a48;
    --red: #e3262b;
    --card: #f2f3f5;
    --backdrop: #e4e6ea;
    --font-text: "Oswald", "Arial Narrow", sans-serif;
  }
  * { margin: 0; padding: 0; box-sizing: border-box; }
  html, body {
    width: 1200px;
    height: 1100px;
    overflow: hidden;
    background: var(--backdrop);
  }
  .canvas {
    position: relative;
    width: 1200px;
    height: 1100px;
    display: flex;
    align-items: center;
  }
  .card-spread {
    position: relative;
    width: 1200px;
    height: 335px;
    background: var(--card);
    font-family: var(--font-text);
    color: var(--navy);
  }

  /* Front side */
  .card-front {
    position: absolute;
    left: 0; top: 0;
    width: 558px; height: 335px;
  }
  .brand-lockup {
    position: absolute;
    left: 50px; top: 60px;
    display: flex;
    align-items: flex-start;
    gap: 18px;
  }
  .brand-square {
    width: 54px; height: 54px;
    background: var(--red);
    margin-top: 10px;
  }
  .brand-name {
    font-weight: 500;
    font-size: 50px;
    line-height: 1;
    color: var(--navy);
    text-transform: uppercase;
  }
  .company-line {
    position: absolute;
    right: 38px; top: 278px;
    font-weight: 400;
    font-size: 16px;
    letter-spacing: 1.2px;
    white-space: nowrap;
  }

  /* Colour divider */
  .divider-band {
    position: absolute;
    left: 558px; top: 0;
    width: 82px; height: 335px;
  }
  .divider-band .band-red  { height: 167px; background: var(--red); }
  .divider-band .band-navy { height: 168px; background: var(--navy); }

  /* Back side */
  .card-back {
    position: absolute;
    left: 640px; top: 0;
    width: 560px; height: 335px;
  }
  .corner-mark {
    position: absolute;
    right: 30px; top: 30px;
    width: 20px; height: 20px;
    background: var(--red);
  }
  .person-name {
    position: absolute;
    left: 40px; top: 26px;
    font-weight: 400;
    font-size: 24px;
    letter-spacing: 1px;
  }
  .person-title {
    position: absolute;
    left: 40px; top: 60px;
    font-weight: 300;
    font-size: 16px;
    letter-spacing: 2.4px;
  }
  .contact-list {
    position: absolute;
    left: 38px; top: 174px;
    list-style: none;
    font-weight: 300;
    font-size: 15px;
    letter-spacing: 1.6px;
    line-height: 21px;
  }
  .contact-list .phone { margin-bottom: 21px; }
  .services {
    position: absolute;
    left: 40px; top: 278px;
    font-weight: 400;
    font-size: 16px;
    letter-spacing: 1.2px;
    white-space: nowrap;
  }
</style>
</head>
<body>
<main class="canvas">
  <section class="card-spread">
    <div class="card-front">
      <div class="brand-lockup">
        <div class="brand-square"></div>
        <div class="brand-name">Harbourline<br>Strategy Group</div>
      </div>
      <p class="company-line">Harbourline Strategy Group Pty Ltd</p>
    </div>

    <div class="divider-band" aria-hidden="true">
      <div class="band-red"></div>
      <div class="band-navy"></div>
    </div>

    <div class="card-back">
      <div class="corner-mark" aria-hidden="true"></div>
      <h1 class="person-name">Daniel Ferreira</h1>
      <p class="person-title">Principal Consultant</p>
      <ul class="contact-list">
        <li class="phone">+61 417 260 315</li>
        <li class="email">daniel@harbourlinestrategygroup.com.au</li>
        <li class="web">www.harbourlinestrategygroup.com</li>
      </ul>
      <p class="services">Professional services: Business Analysis, Strategic Advisory</p>
    </div>
  </section>
</main>
</body>
</html>
```